Business Card Design Project - Harbourline Removals

I need a business card design created for my furniture removal business. The name is Harbourline Removals so something associated with the galaxy would be great ( possibly the southern cross or something to that effect). Modern, creative and simple was what I had in mind. I like metallic silver and different shades of blue but am open to other colour ideas.

Industry/Entity Type

Business

Requirements
Must have
• Something associated with the galaxy
Nice to have
• Have checked out lots of different fontstyles and really like 'kefa'

```html
<!DOCTYPE html>
<html lang="en">
<head>
<meta charset="utf-8">
<title>Harbourline Removals – Business Card</title>
<link rel="stylesheet" href="https://fonts.googleapis.com/css2?family=Source+Sans+3:wght@400;700&display=swap">
<style>
  :root {
    --stage: #000000;
    --silver-light: #f2f3f5;
    --silver-mid: #d3d5d9;
    --silver-dark: #a9acb2;
    --navy: #0e2550;
    --navy-deep: #040f2b;
    --blue-glow: #1d4f8e;
    --ink: #2b2b2b;
    --white: #ffffff;
  }
  * { margin: 0; padding: 0; box-sizing: border-box; }
  html, body {
    width: 1200px; height: 711px; overflow: hidden;
    background: var(--stage);
    font-family: "Source Sans 3", Arial, sans-serif;
  }
  .canvas { position: relative; width: 1200px; height: 711px; }
  .card {
    position: absolute; top: 231px;
    width: 485px; height: 277px; overflow: hidden;
  }
  .card--front {
    left: 96px;
    background: linear-gradient(120deg, var(--silver-mid) 0%, var(--silver-light) 28%, var(--silver-mid) 48%, var(--silver-dark) 70%, var(--silver-light) 100%);
  }
  .card--back {
    left: 620px;
    background: radial-gradient(ellipse 55% 65% at 42% 50%, var(--blue-glow) 0%, var(--navy) 55%, var(--navy-deep) 100%);
  }
  .galaxy-pattern {
    position: absolute; left: 160px; top: 36px; width: 325px; height: 241px;
    background:
      radial-gradient(ellipse 60% 55% at 72% 58%, rgba(255,255,255,0.75) 0%, rgba(255,255,255,0.35) 50%, rgba(255,255,255,0) 100%);
  }
  .brand-dot { position: absolute; border-radius: 50%; }
  .card--front .brand-dot { left: 150px; top: 62px; width: 58px; height: 58px; background: var(--navy); }
  .card--back .brand-dot { left: 146px; top: 96px; width: 82px; height: 82px; background: var(--white); }
  .brand-name { position: absolute; font-weight: 700; white-space: nowrap; line-height: 1; }
  .card--front .brand-name { left: 222px; top: 111px; font-size: 15px; color: var(--navy); }
  .card--back .brand-name { left: 243px; top: 162px; font-size: 21px; color: var(--white); }
  .holder-name {
    position: absolute; left: 35px; top: 219px;
    font-size: 21px; line-height: 24px; color: var(--ink); font-weight: 400;
  }
  .divider {
    position: absolute; left: 162px; top: 206px;
    width: 1px; height: 59px; background: var(--ink);
  }
  .contact {
    position: absolute; left: 174px; top: 213px;
    font-size: 14px; line-height: 18px; color: var(--ink); list-style: none;
  }
</style>
</head>
<body>
<main class="canvas">
  <section class="card card--front">
    <div class="galaxy-pattern" role="img" aria-label="Faint dotted galaxy spiral pattern in soft white"></div>
    <span class="brand-dot"></span>
    <p class="brand-name">Harbourline Removals</p>
    <p class="holder-name">Dane Mercer</p>
    <span class="divider"></span>
    <ul class="contact">
      <li>Phone 0412587306</li>
      <li>Email danemercer@mailbox.com</li>
    </ul>
  </section>
  <section class="card card--back">
    <span class="brand-dot"></span>
    <p class="brand-name">Harbourline Removals</p>
  </section>
</main>
</body>
</html>
```